Website for Excavator and Earthworks Company

We require a modern, sleek and practical website for our newly created earthworks/excavator business in Perth, Western Australia called Gullwind Stonecut Earthworks.

The website should have a modern, cutting edge feel but only needs to be relatively simplistic in it's layout and eventual functionality.

Some pages it should have would be Home, About, Projects and Contact Us.

Number of Pages Required

1 page

```html
<!DOCTYPE html>
<html lang="en">
<head>
<meta charset="utf-8">
<title>Gullwind Stonecut Earthworks</title>
<link href="https://fonts.googleapis.com/css2?family=Krona+One&family=Roboto:wght@400;500;700&display=swap" rel="stylesheet">
<style>
:root{
  --lime:#c4d600;
  --lime-deep:#a9b800;
  --ink:#000000;
  --white:#ffffff;
  --cream:#f6f9e4;
  --tab:#ececec;
  --tab-active:#eef3c4;
  --grey-line:#cfcfcf;
  --text:#111111;
}
*{margin:0;padding:0;box-sizing:border-box}
html,body{width:1200px;height:4717px;overflow:hidden;background:var(--white)}
body{position:relative;font-family:"Roboto",Arial,sans-serif;color:var(--text)}
.display{font-family:"Krona One","Arial Black",sans-serif;text-transform:uppercase}
.abs{position:absolute}
.media{position:absolute;display:block}

/* header */
.site-header{position:absolute;left:0;top:0;width:1200px;height:113px;background:var(--white)}
.brand{position:absolute;left:119px;top:58px;font-family:"Krona One",sans-serif;font-size:17px;color:var(--ink);letter-spacing:0.5px}
.brand-mark{position:absolute;left:172px;top:14px;width:36px;height:36px;background:var(--lime)}
.call-bar{position:absolute;left:687px;top:0;width:394px;height:46px;background:var(--lime);clip-path:polygon(4% 0,100% 0,100% 100%,0 100%)}
.call-bar span{position:absolute;left:80px;top:13px;font-family:"Krona One",sans-serif;font-size:18px;color:var(--ink);letter-spacing:1px}
.call-bar svg{position:absolute;left:50px;top:13px}
.nav{position:absolute;top:74px;font-family:"Krona One",sans-serif;font-size:14px;color:var(--ink)}

/* hero */
.hero{position:absolute;left:0;top:113px;width:1200px;height:640px;background:linear-gradient(180deg,#2b3542 0%,#3b3f4a 40%,#5a4d4a 62%,#3b3630 80%,#2a2622 100%)}
.hero-title{position:absolute;right:119px;top:270px;text-align:right;font-size:52px;line-height:60px;color:var(--white)}
.hero-btn{position:absolute;left:910px;top:412px;width:170px;height:46px;background:var(--lime);clip-path:polygon(8% 0,100% 0,92% 100%,0 100%);font-size:17px;color:var(--ink);text-align:center;line-height:46px}

/* welcome */
.welcome-title{position:absolute;left:0;width:1200px;text-align:center;color:var(--ink)}
.rule{position:absolute;height:2px;background:var(--lime)}
.intro-heading{position:absolute;left:119px;top:955px;font-size:30px;line-height:34px;color:var(--ink);font-family:"Krona One",sans-serif}
.intro-text{position:absolute;left:119px;top:1078px;width:380px;font-size:16px;line-height:24px;color:var(--ink)}

/* about */
.feature{position:absolute;top:1676px;width:290px}
.feature-icon{width:114px;height:114px;border-radius:50%;background:var(--ink);display:flex;align-items:center;justify-content:center}
.feature h3{margin-top:24px;font-family:"Krona One",sans-serif;font-size:26px;line-height:31px;color:var(--ink);font-weight:400}
.feature p{margin-top:26px;font-size:14.5px;line-height:22.5px;color:var(--ink)}

/* latest projects */
.section-title{position:absolute;font-size:38px;line-height:46px;color:var(--ink)}
.lead{position:absolute;left:449px;top:2276px;width:640px;font-size:25px;line-height:32px;color:var(--ink)}
.tab{position:absolute;left:119px;height:54px;border-radius:6px;background:var(--tab);font-weight:700;font-size:17px;letter-spacing:0.5px;line-height:54px;padding-left:24px;color:#222}
.tab.is-active{background:var(--tab-active)}
.desc-title{position:absolute;left:119px;top:2697px;font-weight:700;font-size:19px;letter-spacing:1px}
.desc-loc{position:absolute;left:119px;top:2750px;font-size:14px;color:var(--lime-deep)}
.desc-text{position:absolute;left:119px;top:2778px;width:285px;font-size:15.5px;line-height:23.5px}

/* completed */
.card{position:absolute;top:3233px;width:297px;height:434px;border:2px solid #222;background:var(--white)}
.card .media{left:0;top:0;width:293px;height:229px}
.card-date{position:absolute;left:27px;top:262px;font-size:14px;font-weight:500;color:var(--lime-deep)}
.card-title{position:absolute;left:27px;top:300px;width:250px;font-size:23px;line-height:29px;font-weight:500;color:var(--ink)}

/* contact */
.contact-sub{position:absolute;left:0;top:3960px;width:1200px;text-align:center;font-size:13.5px;line-height:20px;color:var(--ink)}
.field{position:absolute;background:var(--white);border-radius:3px;font-size:14px;padding:10px 12px;color:var(--ink)}
.submit{position:absolute;left:526px;top:4182px;width:150px;height:50px;background:var(--ink);color:var(--white);font-family:"Krona One",sans-serif;font-size:14px;text-align:center;line-height:50px}

/* footer */
.footer-brand{position:absolute;left:119px;top:4470px;width:290px;text-align:center;font-family:"Krona One",sans-serif;font-size:24px;color:var(--white);line-height:32px}
.social{position:absolute;top:4560px;width:44px;height:44px;border-radius:50%;background:var(--lime)}
.col-head{position:absolute;top:4383px;font-family:"Krona One",sans-serif;font-size:19px;color:var(--lime)}
.links{position:absolute;left:535px;top:4428px;list-style:none;font-size:14px;line-height:23px;color:var(--white)}
.addr{position:absolute;left:784px;font-size:14px;line-height:20px;color:var(--white);display:flex;align-items:flex-start;gap:12px}
.addr i{flex:none;width:28px;height:28px;border:1.5px solid var(--white);border-radius:50%;display:flex;align-items:center;justify-content:center}
.vline{position:absolute;top:4380px;width:1px;height:240px;background:#c4d600}
.copyright{position:absolute;left:0;top:4662px;width:1200px;text-align:center;font-size:12.5px;color:var(--white)}
</style>
</head>
<body>

<header class="site-header">
  <div class="brand-mark"></div>
  <div class="brand">GULLWIND STONECUT</div>
  <div class="call-bar">
    <svg width="20" height="20" viewBox="0 0 24 24"><path d="M6.6 10.8a15 15 0 0 0 6.6 6.6l2.2-2.2a1 1 0 0 1 1-.25 11.4 11.4 0 0 0 3.6.57 1 1 0 0 1 1 1V20a1 1 0 0 1-1 1A17 17 0 0 1 3 4a1 1 0 0 1 1-1h3.5a1 1 0 0 1 1 1c0 1.25.2 2.45.57 3.6a1 1 0 0 1-.25 1z" fill="#000"/></svg>
    <span>CALLUS: 08 5550 1742</span>
  </div>
  <nav>
    <span class="nav" style="left:516px">HOME</span>
    <span class="nav" style="left:641px">ABOUT</span>
    <span class="nav" style="left:777px">PROJECTS</span>
    <span class="nav" style="left:952px">CONTACT US</span>
  </nav>
</header>

<section class="hero">
  <div class="media" role="img" aria-label="Excavator on a construction site under a stormy sky" style="left:0;top:0;width:1200px;height:640px;background:linear-gradient(100deg,rgba(60,50,30,.55) 0%,rgba(180,130,40,.25) 25%,rgba(0,0,0,0) 45%)"></div>
  <h1 class="hero-title display">Gullwind Stonecut<br>Earthworks</h1>
  <div class="hero-btn display">Contact</div>
  <svg class="abs" style="left:0;top:500px" width="1200" height="140" viewBox="0 0 1200 140">
    <polygon points="0,110 522,75 1200,140 0,140" fill="#ffffff"/>
    <polygon points="522,75 1200,15 1200,140" fill="#c4d600"/>
  </svg>
</section>

<h2 class="welcome-title display" style="top:790px;font-size:38px">Welcome To</h2>
<p class="welcome-title display" style="top:835px;font-size:28px">Gullwind Stonecut Earthworks</p>
<div class="rule" style="left:527px;top:879px;width:147px;height:2px"></div>

<h2 class="intro-heading">Excavator<br>and Earthworks<br>Company</h2>
<p class="intro-text">Lorem ipsum dolor sit amet, consectetur adipiscing elit, sed do eiusmod tempor incididunt ut labore et dolore magna aliqua. Quis ipsum suspendisse ultr ices gravida. Risus commodo viverra maecenas accumsan lacus vel facilisis. Lorem ipsum dolor sit amet, consectetur adipiscing elit, sed do eiusmod tempor incididunt ut labore et dolore magna aliqua. Quis ipsum suspendisse ultrices gravida. Risus commodo viverra maecenas accumsan lacus vel facilisis.</p>
<div class="media" role="img" aria-label="Yellow excavator in front of a lime green tinted earthworks photo panel" style="left:522px;top:940px;width:605px;height:412px;background:linear-gradient(135deg,#9bb300 0%,#c4d600 45%,#e7f07a 70%,#ffffff 100%)"></div>

<section class="about">
  <svg class="abs" style="left:0;top:1395px" width="1200" height="750" viewBox="0 0 1200 750">
    <polygon points="0,6 1200,116 1200,750 0,750" fill="#c4d600"/>
    <polygon points="513,50 1200,6 1200,116" fill="#000"/>
  </svg>
  <div class="media" role="img" aria-label="Faint earthworks site photo under a lime green overlay" style="left:0;top:1600px;width:1200px;height:543px;background:linear-gradient(180deg,rgba(196,214,0,0) 0%,rgba(150,165,0,.35) 60%,rgba(196,214,0,.2) 100%)"></div>
  <h2 class="welcome-title display" style="top:1557px;font-size:38px;line-height:44px">About Gullwind<br>Stonecut Earthworks</h2>

  <div class="feature" style="left:119px">
    <div class="feature-icon"><svg width="60" height="60" viewBox="0 0 24 24"><path d="M12 2a7 7 0 0 0-7 7c0 5 7 13 7 13s7-8 7-13a7 7 0 0 0-7-7z" fill="#c4d600"/><path d="M12 5.5l-4 3.3V13h2.7v-2.5h2.6V13H16V8.8z" fill="#000"/></svg></div>
    <h3>Lorem ipsum<br>dolor sit amet,</h3>
    <p>Lorem ipsum dolor sit amet, consectetur adipiscing elit, sed do eiusmod tempor incididunt ut labore et dolore magnlora aliqua. Quis ipsum suspendisse ultrice sgravidas commodo viverra.</p>
  </div>
  <div class="feature" style="left:473px">
    <div class="feature-icon"><svg width="60" height="60" viewBox="0 0 24 24"><path d="M12 2l8 3v6c0 5-3.5 9.5-8 11-4.5-1.5-8-6-8-11V5z" fill="#c4d600"/><path d="M8 12l3 3 5-6" stroke="#000" stroke-width="2.2" fill="none"/></svg></div>
    <h3>Lorem ipsum<br>dolor sit amet,</h3>
    <p>Lorem ipsum dolor sit amet, consectetur adipiscing elit, sed do eiusmod tempor incididunt ut labore et dolore magnlora aliqua. Quis ipsum suspendisse ultrice sgravidas commodo viverra.</p>
  </div>
  <div class="feature" style="left:810px">
    <div class="feature-icon"><svg width="60" height="60" viewBox="0 0 24 24"><path d="M9 3h6l-2 4h-2z" fill="#c4d600"/><path d="M11 7h2c4 3 7 7 7 10a4 4 0 0 1-4 4H8a4 4 0 0 1-4-4c0-3 3-7 7-10z" fill="#c4d600"/><text x="12" y="18.5" text-anchor="middle" font-family="Roboto,Arial,sans-serif" font-weight="700" font-size="9" fill="#000">$</text></svg></div>
    <h3>Lorem ipsum<br>dolor sit amet,</h3>
    <p>Lorem ipsum dolor sit amet, consectetur adipiscing elit, sed do eiusmod tempor incididunt ut labore et dolore magnlora aliqua. Quis ipsum suspendisse ultrice sgravidas commodo viverra.</p>
  </div>
</section>

<section class="latest">
  <h2 class="section-title display" style="left:119px;top:2272px">Latest<br>Projects</h2>
  <div class="rule" style="left:119px;top:2370px;width:153px;height:3px"></div>
  <p class="lead">Lorem ipsum dolor sit amet, consectetur adipiscingeli sed do eiusmod tempor incididunt ut labore et lordolor uis ipsum suspendisse.</p>
  <div class="abs" style="left:119px;top:2414px;width:962px;height:1px;background:var(--grey-line)"></div>

  <div class="tab is-active" style="top:2472px;width:208px">PROJECT NAME</div>
  <div class="tab" style="top:2539px;width:245px">PROJECT NAME NEW</div>
  <div class="tab" style="top:2603px;width:223px">PROJECT NAME</div>
  <div class="desc-title">DESCRIPTION</div>
  <div class="abs" style="left:119px;top:2731px;width:262px;height:1px;background:var(--grey-line)"></div>
  <div class="desc-loc">Perth, Western Australia</div>
  <p class="desc-text">Lorem ipsum dolor sit amet, consec tetur adipiscing elit, sed do eiusmod tempor incididunt ut labore et dolore magna aliqua.</p>

  <div class="media" role="img" aria-label="Project video still of a yellow excavator lifting its arm at sunset" style="left:443px;top:2470px;width:636px;height:428px;border-radius:10px;background:linear-gradient(160deg,#3d4a5c 0%,#8a7a6a 40%,#c9a36a 60%,#6a4a30 85%,#3a2a1c 100%)"></div>
  <svg class="abs" style="left:710px;top:2636px" width="96" height="96" viewBox="0 0 96 96">
    <circle cx="48" cy="48" r="43" fill="none" stroke="#fff" stroke-width="6"/>
    <polygon points="38,28 70,48 38,68" fill="#fff"/>
  </svg>
</section>

<section class="completed">
  <svg class="abs" style="left:0;top:2995px" width="1200" height="810" viewBox="0 0 1200 810">
    <polygon points="0,10 1200,40 1200,810 0,810" fill="#f6f9e4"/>
  </svg>
  <h2 class="welcome-title display" style="top:3145px;font-size:38px">Completed Projects</h2>

  <article class="card" style="left:119px">
    <div class="media" role="img" aria-label="Aerial view of an excavator loading a tipper truck" style="background:linear-gradient(135deg,#6b5a48,#8c7a64 50%,#5a4a3a)"></div>
    <div class="card-date">JAN 12 2026</div>
    <h3 class="card-title">Lorem ipsum dolor sit sectetur adipiscing elit, sed do eiusm</h3>
  </article>
  <article class="card" style="left:450px">
    <div class="media" role="img" aria-label="Orange excavator digging red earth under a cloudy sky" style="background:linear-gradient(170deg,#7f8a98 0%,#c2b6a4 40%,#c26a2a 70%,#6a3a20 100%)"></div>
    <div class="card-date">JAN 12 2026</div>
    <h3 class="card-title">Lorem ipsum dolor sit sectetur adipiscing elit, sed do eiusm</h3>
  </article>
  <article class="card" style="left:781px">
    <div class="media" role="img" aria-label="Yellow excavator on a dirt mound at dusk" style="background:linear-gradient(170deg,#4a5a70 0%,#9a8a70 45%,#caa040 65%,#5a4630 100%)"></div>
    <div class="card-date">JAN 12 2026</div>
    <h3 class="card-title">Lorem ipsum dolor sit sectetur adipiscing elit, sed do eiusm</h3>
  </article>
</section>

<section class="contact">
  <svg class="abs" style="left:0;top:3770px" width="1200" height="560" viewBox="0 0 1200 560">
    <polygon points="0,70 1200,90 1200,560 0,560" fill="#c4d600"/>
    <polygon points="467,50 1200,4 1200,90" fill="#000"/>
  </svg>
  <h2 class="welcome-title display" style="top:3908px;font-size:38px">Contact Us</h2>
  <p class="contact-sub">Lorem ipsum dolor sit amet, consectetur adipiscing elit, sed do eiusmod tem<br>orincididunt ut labore et dolore magna aliquipsum suspendisravida.</p>
  <div class="media" role="img" aria-label="Yellow excavator with raised arm" style="left:27px;top:3975px;width:229px;height:303px;background:linear-gradient(160deg,rgba(230,200,60,.9) 0%,#d9b230 50%,#4a4a3a 100%);clip-path:polygon(55% 0,80% 20%,70% 70%,100% 80%,90% 100%,0 100%,5% 80%,30% 60%)"></div>
  <div class="field" style="left:302px;top:4025px;width:277px;height:42px">Name:</div>
  <div class="field" style="left:302px;top:4077px;width:277px;height:42px">Phone:</div>
  <div class="field" style="left:302px;top:4129px;width:277px;height:42px">Email:</div>
  <div class="field" style="left:590px;top:4025px;width:308px;height:146px">Message:</div>
  <div class="submit">SUBMIT NOW</div>
</section>

<footer class="site-footer">
  <svg class="abs" style="left:0;top:4290px" width="1200" height="427" viewBox="0 0 1200 427">
    <polygon points="0,20 1200,5 1200,427 0,427" fill="#000"/>
  </svg>
  <div class="footer-brand">GULLWIND<br>STONECUT</div>
  <div class="social" style="left:214px"></div>
  <div class="social" style="left:267px"></div>
  <div class="vline" style="left:467px"></div>
  <div class="vline" style="left:714px"></div>
  <div class="col-head" style="left:535px">LINKS</div>
  <ul class="links">
    <li>Home</li><li>About Us</li><li>Projects</li><li>Completed Projects</li><li>Contact</li>
  </ul>
  <div class="col-head" style="left:784px">OUR ADDRESS:</div>
  <div class="addr" style="top:4430px"><i><svg width="14" height="14" viewBox="0 0 24 24"><path d="M12 2a7 7 0 0 0-7 7c0 5 7 13 7 13s7-8 7-13a7 7 0 0 0-7-7zm0 9.5A2.5 2.5 0 1 1 12 6.5a2.5 2.5 0 0 1 0 5z" fill="#fff"/></svg></i><span>18 Quarry Ridge Road<br>Perth, Western Australia</span></div>
  <div class="addr" style="top:4482px"><i><svg width="14" height="14" viewBox="0 0 24 24"><path d="M6.6 10.8a15 15 0 0 0 6.6 6.6l2.2-2.2a1 1 0 0 1 1-.25 11.4 11.4 0 0 0 3.6.57 1 1 0 0 1 1 1V20a1 1 0 0 1-1 1A17 17 0 0 1 3 4a1 1 0 0 1 1-1h3.5a1 1 0 0 1 1 1c0 1.25.2 2.45.57 3.6a1 1 0 0 1-.25 1z" fill="#fff"/></svg></i><span style="padding-top:4px">Phone: (08) 5550 3814</span></div>
  <div class="addr" style="top:4527px"><i><svg width="14" height="14" viewBox="0 0 24 24"><rect x="3" y="5" width="18" height="14" rx="2" fill="none" stroke="#fff" stroke-width="2"/><path d="M3 7l9 6 9-6" fill="none" stroke="#fff" stroke-width="2"/></svg></i><span style="padding-top:4px">info@gullwindstonecut.com.au</span></div>
  <div class="abs" style="left:119px;top:4642px;width:962px;height:1px;background:#333"></div>
  <p class="copyright">© 2026 Gullwind Stonecut Earthworks.. All Rights are Reserved</p>
</footer>

</body>
</html>
```